Birchline Septic Solutions

Would like to see some single sided ones but would also like to see some double sided with one sided only being the logo. Owners name is Tom Waldrick. Phone number is 555-214-8830
Services are pumping, inspections, installs, and repairs

Contact Information for Business Card

555-241-8830 Tom Waldrick Alderbrook, OH

```html
<!DOCTYPE html>
<html lang="en">
<head>
<meta charset="utf-8">
<title>Birchline Septic Solutions – Business Cards</title>
<link rel="stylesheet" href="https://fonts.googleapis.com/css2?family=Open+Sans:wght@400;600;700;800&display=swap">
<style>
  :root {
    --bg: #232323;
    --card: #222226;
    --card-edge: #25c1bd;
    --teal: #27c0bc;
    --white: #ffffff;
    --deep: #111113;
    --scenery-top: rgba(60,60,62,0);
    --scenery-bottom: #2e2e31;
  }
  * { box-sizing: border-box; margin: 0; padding: 0; }
  html, body { width: 1200px; height: 779px; overflow: hidden; background: var(--bg); }
  body { font-family: "Open Sans", Arial, sans-serif; position: relative; }

  .card {
    position: absolute;
    width: 540px;
    height: 309px;
    background: var(--card);
    border-bottom: 4px solid var(--card-edge);
    border-left: 3px solid var(--card-edge);
    box-shadow: 0 14px 30px rgba(0,0,0,.55);
    overflow: hidden;
  }
  .card--back { left: 40px; top: 235px; }
  .card--front { left: 620px; top: 235px; }

  /* Back: wordmark only */
  .back-mark {
    position: absolute; inset: 0;
    display: flex; flex-direction: column; align-items: center; justify-content: center;
    color: var(--deep);
    font-weight: 800;
    text-align: center;
    line-height: 1.05;
  }
  .back-mark__name { font-size: 62px; letter-spacing: 1px; }
  .back-mark__sub { font-size: 21px; letter-spacing: 7px; text-transform: uppercase; }

  /* Front: contact */
  .contact {
    position: absolute; top: 26px; right: 46px;
    text-align: right; color: var(--white);
  }
  .contact__name { font-size: 25px; font-weight: 700; line-height: 1.1; }
  .contact__first { color: var(--teal); font-weight: 600; }
  .contact__line { font-size: 13px; line-height: 1.45; }
  .contact__phone { display: inline-flex; align-items: center; gap: 6px; }
  .contact__phone svg { width: 12px; height: 12px; fill: var(--teal); }
  .contact-bar {
    position: absolute; top: 26px; right: 18px;
    width: 15px; height: 62px; background: var(--teal);
  }

  /* Front: wordmark */
  .wordmark {
    position: absolute; left: 48px; top: 106px;
    color: var(--white); font-weight: 800; line-height: 1.05;
  }
  .wordmark__name { font-size: 46px; letter-spacing: .5px; }
  .wordmark__sub { font-size: 15px; letter-spacing: 5px; text-transform: uppercase; }

  /* Front: services */
  .services {
    position: absolute; left: 92px; top: 208px; color: var(--white);
  }
  .services__title { color: var(--teal); font-weight: 700; font-size: 14px; letter-spacing: .5px; }
  .services__list { list-style: none; font-size: 13.5px; line-height: 1.28; }
  .services__list li { display: flex; align-items: center; gap: 8px; }
  .services__list li::before {
    content: ""; width: 8px; height: 8px; border-radius: 50%; background: var(--teal);
  }

  .scenery {
    position: absolute; right: 0; bottom: 0;
    width: 270px; height: 150px;
    background: linear-gradient(180deg, var(--scenery-top) 0%, var(--scenery-bottom) 100%);
  }
</style>
</head>
<body>
  <section class="card card--back" aria-label="Card back">
    <div class="back-mark">
      <span class="back-mark__name">Birchline</span>
      <span class="back-mark__sub">Septic Solutions</span>
    </div>
  </section>

  <section class="card card--front" aria-label="Card front">
    <div class="scenery" role="img" aria-label="Dark mountain and pine tree scenery"></div>

    <div class="contact">
      <p class="contact__name"><span class="contact__first">Tom</span> Waldrick</p>
      <p class="contact__line">Alderbrook, OH</p>
      <p class="contact__line contact__phone">555-241-8830
        <svg viewBox="0 0 24 24" aria-hidden="true"><path d="M6.6 10.8a15.1 15.1 0 0 0 6.6 6.6l2.2-2.2a1 1 0 0 1 1-.25 11.4 11.4 0 0 0 3.6.57 1 1 0 0 1 1 1V20a1 1 0 0 1-1 1A17 17 0 0 1 3 4a1 1 0 0 1 1-1h3.5a1 1 0 0 1 1 1c0 1.25.2 2.45.57 3.6a1 1 0 0 1-.25 1z"/></svg>
      </p>
    </div>
    <div class="contact-bar"></div>

    <div class="wordmark">
      <p class="wordmark__name">Birchline</p>
      <p class="wordmark__sub">Septic Solutions</p>
    </div>

    <div class="services">
      <p class="services__title">SERVICES</p>
      <ul class="services__list">
        <li>Pumping</li>
        <li>Inspections</li>
        <li>Installs</li>
        <li>And Repairs</li>
      </ul>
    </div>
  </section>
</body>
</html>
```